Bref créative
BRISK FIELD Stationery
Stationery for BRISKFIELD web site
Professional
Tomas Kerbrune
7 Rue Montaleur, Res. Les Pins
Hendaye
info@briskfield-exemple.com
www.briskfield-exemple.com

```html
<!DOCTYPE html>
<html lang="fr">
<head>
<meta charset="utf-8">
<title>BRISK FIELD Stationery</title>
<link rel="stylesheet" href="https://fonts.googleapis.com/css2?family=Exo+2:wght@400;700&family=Oswald:wght@300&display=swap">
<style>
  :root {
    --backdrop: #3a3a3a;
    --panel: #1c1c1c;
    --paper: #f4f4f4;
    --accent: #d9411e;
    --accent-light: #f08a3a;
    --ink: #6a6a6a;
    --label: #bdbdbd;
  }
  * { margin: 0; padding: 0; box-sizing: border-box; }
  html, body { width: 1200px; height: 600px; overflow: hidden; }
  body {
    background: var(--backdrop);
    font-family: "Exo 2", sans-serif;
    position: relative;
  }
  .piece { position: absolute; background: var(--paper); overflow: hidden; box-shadow: 0 3px 8px rgba(0,0,0,.45); }
  .piece svg.shape { position: absolute; inset: 0; width: 100%; height: 100%; }
  .label {
    position: absolute;
    font-family: "Oswald", sans-serif;
    font-weight: 300;
    font-size: 11px;
    letter-spacing: .5px;
    color: var(--label);
  }
  .brand {
    position: absolute;
    display: flex;
    align-items: center;
    gap: 5px;
    font-weight: 700;
    color: #ffffff;
    letter-spacing: .5px;
    white-space: nowrap;
  }
  .brand .dot { border-radius: 50%; background: var(--accent); flex: none; }
  .contact { position: absolute; color: var(--ink); line-height: 1.6; }
  .contact li { list-style: none; display: flex; align-items: center; gap: 5px; white-space: nowrap; }
  .contact svg { flex: none; }

  /* letterhead */
  .letterhead { left: 259px; top: 24px; width: 401px; height: 547px; }
  .letterhead .brand { left: 52px; top: 34px; font-size: 17px; }
  .letterhead .brand .dot { width: 12px; height: 12px; }
  .letterhead .contact { left: 300px; top: 12px; font-size: 6px; }
  .watermark {
    position: absolute; left: 150px; top: 430px; width: 150px; height: 150px;
    border-radius: 50%; background: #e4e4e4;
    display: flex; align-items: center; justify-content: center;
    font-weight: 700; font-size: 19px; color: #ececec;
  }

  /* business cards */
  .card { left: 34px; width: 115px; height: 60px; }
  .card-front { top: 233px; }
  .card-back { top: 324px; background: var(--panel); }
  .card-front .brand { left: 8px; top: 8px; font-size: 8px; }
  .card-front .brand .dot { width: 6px; height: 6px; }
  .card-front .contact { left: 8px; top: 28px; font-size: 3.5px; color: #cfcfcf; line-height: 1.7; }
  .card-front .holder { position: absolute; right: 6px; top: 40px; font-size: 4px; color: var(--ink); }
  .card-back .brand { left: 22px; top: 22px; font-size: 12px; }
  .card-back .brand .dot { width: 9px; height: 9px; }

  /* envelope */
  .envelope { left: 696px; top: 79px; width: 480px; height: 233px; }
  .envelope .brand { left: 180px; top: 58px; font-size: 15px; }
  .envelope .brand .dot { width: 11px; height: 11px; }

  /* compliment slip */
  .slip { left: 696px; top: 372px; width: 264px; height: 120px; }
  .slip .brand { left: 14px; top: 14px; font-size: 11px; }
  .slip .brand .dot { width: 8px; height: 8px; }
  .slip .contact { left: 188px; top: 14px; font-size: 4.5px; }
</style>
</head>
<body>

  <p class="label" style="left:34px; top:210px;">Stationery Concept</p>

  <!-- business card front -->
  <section class="piece card card-front">
    <svg class="shape" viewBox="0 0 115 60" preserveAspectRatio="none">
      <path d="M0 0 H78 Q62 34 48 60 H0 Z" fill="var(--panel)"/>
      <path d="M78 0 Q62 34 48 60" fill="none" stroke="var(--accent)" stroke-width="1.6"/>
    </svg>
    <div class="brand"><span class="dot"></span>BRISKFIELD</div>
    <ul class="contact">
      <li>+33 600 12 34 56</li>
      <li>info@briskfield-exemple.com</li>
      <li>www.briskfield-exemple.com</li>
    </ul>
    <p class="holder">Tomas Kerbrune</p>
  </section>
  <p class="label" style="left:40px; top:298px;">Business Card Front</p>

  <!-- business card back -->
  <section class="piece card card-back">
    <svg class="shape" viewBox="0 0 115 60" preserveAspectRatio="none">
      <path d="M100 0 Q90 34 80 60" fill="none" stroke="var(--accent)" stroke-width="1.2" opacity=".7"/>
    </svg>
    <div class="brand"><span class="dot"></span>BRISKFIELD</div>
  </section>
  <p class="label" style="left:40px; top:390px;">Business Card Back</p>

  <!-- letterhead -->
  <section class="piece letterhead">
    <svg class="shape" viewBox="0 0 401 547" preserveAspectRatio="none">
      <defs>
        <linearGradient id="edge" x1="0" y1="0" x2="0" y2="1">
          <stop offset="0" stop-color="var(--accent-light)"/>
          <stop offset="1" stop-color="var(--accent)"/>
        </linearGradient>
      </defs>
      <path d="M0 0 H165 Q40 230 0 470 Z" fill="var(--panel)"/>
      <path d="M165 0 Q40 230 0 470" fill="none" stroke="url(#edge)" stroke-width="4"/>
    </svg>
    <div class="brand"><span class="dot"></span>BRISKFIELD</div>
    <ul class="contact">
      <li><svg width="6" height="6" viewBox="0 0 10 10"><circle cx="5" cy="5" r="5" fill="var(--accent)"/></svg>+33 600 12 34 56</li>
      <li><svg width="6" height="6" viewBox="0 0 10 10"><circle cx="5" cy="5" r="5" fill="var(--accent)"/></svg>info@briskfield-exemple.com</li>
      <li><svg width="6" height="6" viewBox="0 0 10 10"><circle cx="5" cy="5" r="5" fill="var(--accent)"/></svg>www.briskfield-exemple.com</li>
    </ul>
    <div class="watermark">BRISKFIELD</div>
  </section>
  <p class="label" style="left:405px; top:576px;">Letter head Option 1</p>

  <!-- envelope -->
  <section class="piece envelope">
    <svg class="shape" viewBox="0 0 480 233" preserveAspectRatio="none">
      <path d="M0 0 H480 V60 Q300 120 0 233 Z" fill="var(--panel)"/>
      <path d="M480 60 Q300 120 0 233" fill="none" stroke="var(--accent)" stroke-width="3"/>
    </svg>
    <div class="brand"><span class="dot"></span>BRISKFIELD</div>
  </section>

  <!-- compliment slip -->
  <section class="piece slip">
    <svg class="shape" viewBox="0 0 264 120" preserveAspectRatio="none">
      <path d="M0 0 H120 Q60 60 0 110 Z" fill="var(--panel)"/>
      <path d="M120 0 Q60 60 0 110" fill="none" stroke="var(--accent)" stroke-width="2.5"/>
    </svg>
    <div class="brand"><span class="dot"></span>BRISKFIELD</div>
    <ul class="contact">
      <li><svg width="5" height="5" viewBox="0 0 10 10"><circle cx="5" cy="5" r="5" fill="var(--accent)"/></svg>+33 600 12 34 56</li>
      <li><svg width="5" height="5" viewBox="0 0 10 10"><circle cx="5" cy="5" r="5" fill="var(--accent)"/></svg>info@briskfield-exemple.com</li>
      <li><svg width="5" height="5" viewBox="0 0 10 10"><circle cx="5" cy="5" r="5" fill="var(--accent)"/></svg>www.briskfield-exemple.com</li>
    </ul>
  </section>
  <p class="label" style="left:862px; top:512px;">Envelope Option 2</p>

</body>
</html>
```